Business Card: RW Office Partners - Your tidy answer finder

Business Name: RW Office Partners
Website: www.rwofficepartners.com.au
Email: marisol@rwofficepartners.com.au
Mobile: 61 487 902 346
Facebook: @rwofficepartners
Instrgram: @rwofficepartners

Brading Colours:
HEX
#986474
#ddccd3
#7a8498
#c9d8e4
#000000
#ffffff

Tag Line: Your organised problem solver

Link to DRAFT website:
https://helpdeskhub.sitebuilderx.com/rw-office-partners

About Page from the website:
My name is Marisol Bramwell, and I would love to assist you to become more productive in your day to day and achieve your business and personal goals.
My mission is to give you time, time to work on the important tasks of your business or to be able to spend more time with your family. I will take on the tasks you don’t have time for, don’t know well or simply don’t like to do.
I have an extensive background in Administration, Tender Coordination, Document Control, WHS and Quality Management working primarily in the Construction, Mining and Corporate World.
I am passionate about being organised, having order and making things in your life (and mine) easier! I love to watch something unfold and grow into something amazing! I am known for being the go-to problem solver, the organiser of all things, producing high standards of work even under pressure. I’m also a confident communicator, and I understand that you’re busy running your business.

Target Market(s)

Small to Medium Business who require assistance in their business by a virtual assistant.

Industry/Entity Type

Virtual Assistant

Contact Information for Business Card

Mobile: 61 487 902 346

Font styles to use
Sans Serif

Colors
ffffff

Requirements
Must have
• Branding Colours as outlined.
Contact Details as outlined.
Logo as provided.
Proper contact details - mobile, facebook, instragm, website.
Simple, Elegant, very clean looking.
Should not have
• Note cute with pictures.
Not too girly as still want to market to construction companies.

```html
<!DOCTYPE html>
<html lang="en">
<head>
<meta charset="utf-8">
<title>RW Office Partners – Business Card</title>
<link rel="stylesheet" href="https://fonts.googleapis.com/css2?family=Montserrat:wght@400;500;600&family=Roboto:wght@400;500;700&display=swap">
<style>
  :root {
    --plum: #986474;
    --plum-deep: #8a5668;
    --blush: #ddccd3;
    --slate: #7a8498;
    --mist: #c9d8e4;
    --ink: #222222;
    --paper: #ffffff;
    --backdrop: #ebe9e7;
  }
  * { box-sizing: border-box; margin: 0; padding: 0; }
  html, body { width: 1200px; height: 959px; overflow: hidden; }
  body { background: var(--backdrop); position: relative; font-family: "Roboto", Arial, sans-serif; }

  .card {
    position: absolute;
    width: 540px;
    height: 310px;
    box-shadow: 0 6px 18px rgba(0,0,0,0.12);
    overflow: hidden;
  }

  /* Front */
  .card--front { left: 80px; top: 90px; background: var(--plum-deep); color: var(--paper); }
  .front-brand {
    position: absolute; left: 0; right: 0; top: 112px;
    text-align: center;
    font-family: "Montserrat", Arial, sans-serif;
    font-weight: 500; font-size: 34px; letter-spacing: 1px;
    text-transform: uppercase;
  }
  .front-tagline {
    position: absolute; left: 0; right: 0; bottom: 48px;
    text-align: center;
    font-family: "Montserrat", Arial, sans-serif;
    font-size: 11px; letter-spacing: 4px; text-transform: uppercase;
  }

  /* Back */
  .card--back { left: 580px; top: 540px; background: var(--paper); }
  .back-brand {
    position: absolute; left: 34px; top: 130px; width: 200px;
    font-family: "Montserrat", Arial, sans-serif;
    font-weight: 500; font-size: 24px; line-height: 1.05;
    color: var(--plum); text-transform: uppercase;
  }
  .divider { position: absolute; left: 250px; top: 70px; width: 1.5px; height: 150px; background: var(--plum); }
  .contact { position: absolute; left: 268px; top: 68px; }
  .contact-name { font-weight: 700; font-size: 19px; color: var(--plum); }
  .contact-role { font-weight: 700; font-size: 12px; color: var(--ink); margin-bottom: 12px; }
  .contact-line { display: flex; align-items: center; gap: 8px; font-size: 12.5px; color: var(--ink); line-height: 20px; }
  .contact-line svg { width: 12px; height: 12px; flex: none; }
  .social-mark { width: 11px; height: 11px; background: var(--plum); flex: none; }

  .band { position: absolute; left: 0; right: 0; bottom: 0; height: 22px; background: var(--plum); }
  .swatches { position: absolute; right: 0; bottom: 22px; display: flex; }
  .swatches span { width: 30px; height: 6px; }
</style>
</head>
<body>

<section class="card card--front" aria-label="Business card front">
  <p class="front-brand">RW Office Partners</p>
  <p class="front-tagline">Your tidy answer finder</p>
</section>

<section class="card card--back" aria-label="Business card back">
  <p class="back-brand">RW Office Partners</p>
  <div class="divider"></div>
  <div class="contact">
    <p class="contact-name">Marisol Bramwell</p>
    <p class="contact-role">Director</p>
    <p class="contact-line">
      <svg viewBox="0 0 12 12"><rect x="3" y="0.5" width="6" height="11" rx="1" fill="none" stroke="#986474" stroke-width="1.2"/><circle cx="6" cy="9.6" r="0.7" fill="#986474"/></svg>
      61 487 902 346
    </p>
    <p class="contact-line">
      <svg viewBox="0 0 12 12"><rect x="0.6" y="2.5" width="10.8" height="7.5" fill="none" stroke="#986474" stroke-width="1.2"/><path d="M0.6 2.5 L6 7 L11.4 2.5" fill="none" stroke="#986474" stroke-width="1.2"/></svg>
      marisol@rwofficepartners.com.au
    </p>
    <p class="contact-line">
      <svg viewBox="0 0 12 12"><circle cx="6" cy="6" r="5.2" fill="none" stroke="#986474" stroke-width="1.2"/><ellipse cx="6" cy="6" rx="2.2" ry="5.2" fill="none" stroke="#986474" stroke-width="1"/><line x1="0.8" y1="6" x2="11.2" y2="6" stroke="#986474" stroke-width="1"/></svg>
      www.rwofficepartners.com.au
    </p>
    <p class="contact-line">
      <span class="social-mark" aria-hidden="true"></span>
      @rwofficepartners
    </p>
  </div>
  <div class="swatches" aria-hidden="true">
    <span style="background:var(--blush)"></span>
    <span style="background:var(--slate)"></span>
    <span style="background:var(--mist)"></span>
    <span style="background:var(--blush)"></span>
  </div>
  <div class="band"></div>
</section>

</body>
</html>
```